Gritty, Modern True Crime Podcast Launch

Launching a new true crime podcast and are looking for some designs. We are targeting the color scheme of black and red and are looking for both a "noir" and modern vibe. Here is a great example of a current podcast (and look) we love: http://brackenhollowcast.example.The podcast name we like is "Silent Moths." We'd love to go with a rat image (or group of rats) along with some stylized text. Both examples are attached below.

Font styles to use
Serif
Sans Serif

Colors
ec1f27
000000
ffffff
f04a50
1b1b1b

Requirements
Must have
• Rat in design, stylized text, incorporation of primarily red and black colors
Should not have
• photorealistic rats

```html
<!DOCTYPE html>
<html lang="en">
<head>
<meta charset="utf-8">
<title>Silent Moths – Podcast Artwork and Player</title>
<link href="https://fonts.googleapis.com/css2?family=Lato:wght@400;700;900&display=swap" rel="stylesheet">
<style>
  :root {
    --stage: #e4e4e4;
    --panel: #263036;
    --panel-line: #33404a;
    --text: #ffffff;
    --muted: #aab3ba;
    --accent: #1a93e0;
    --track: #3a4650;
    --red: #ec1f27;
    --red-soft: #f04a50;
    --ink: #000000;
    --ink-soft: #1b1b1b;
  }
  * { box-sizing: border-box; margin: 0; padding: 0; }
  html, body { width: 1200px; height: 675px; overflow: hidden; }
  body { background: var(--stage); font-family: "Lato", sans-serif; position: relative; color: var(--text); }

  .art-fill {
    background:
      radial-gradient(ellipse at 28% 24%, rgba(240,74,80,.55), transparent 48%),
      radial-gradient(ellipse at 74% 76%, rgba(236,31,39,.6), transparent 52%),
      linear-gradient(135deg, #3a0d10 0%, var(--ink-soft) 35%, var(--ink) 55%, #2a0709 100%);
    display: flex; align-items: center; justify-content: center; text-align: center;
  }

  .cover-art { position: absolute; left: 177px; top: 115px; width: 446px; height: 446px; }
  .cover-art__title {
    font-weight: 900; font-size: 86px; line-height: .92; color: var(--text);
    text-transform: uppercase; letter-spacing: -1px;
  }

  .player { position: absolute; left: 676px; top: 29px; width: 347px; height: 616px; background: var(--panel); }
  .abs { position: absolute; }
  .status-bar { left: 0; top: 0; width: 100%; height: 22px; font-size: 12px; }
  .status-bar__carrier { left: 8px; top: 4px; display: flex; align-items: center; gap: 5px; }
  .status-bar__time { left: 0; width: 100%; top: 4px; text-align: center; }
  .status-bar__battery { right: 8px; top: 4px; display: flex; align-items: center; gap: 5px; }

  .header__title { left: 0; width: 100%; top: 33px; text-align: center; font-size: 16px; }
  .header__back { left: 19px; top: 35px; }
  .header__search { right: 18px; top: 36px; }

  .episode-art { left: 76px; top: 92px; width: 195px; height: 195px; }
  .episode-art__title {
    font-weight: 900; font-size: 38px; line-height: .92; color: var(--text);
    text-transform: uppercase; letter-spacing: -.5px;
  }

  .episode-meta { left: 0; width: 100%; text-align: center; }
  .episode-meta--tag { top: 341px; font-size: 9.5px; color: var(--muted); }
  .episode-meta--title { top: 363px; font-size: 16px; font-weight: 700; }
  .episode-meta--info { top: 393px; font-size: 9.5px; color: var(--muted); }

  .divider { left: 0; width: 100%; height: 1px; background: var(--panel-line); }

  .transport { left: 0; width: 100%; top: 424px; height: 60px; }
  .progress { left: 22px; width: 303px; top: 509px; height: 4px; border-radius: 2px; background: var(--track); }
  .progress__fill { position: absolute; left: 0; top: 0; width: 196px; height: 4px; border-radius: 2px; background: var(--accent); }
  .progress__handle { position: absolute; left: 195px; top: -4px; width: 3px; height: 12px; background: var(--text); }
  .time { top: 530px; font-size: 10px; }
  .time--elapsed { left: 21px; }
  .time--total { right: 22px; }

  .volume { left: 106px; width: 164px; top: 588px; height: 4px; border-radius: 2px; background: var(--track); }
  .volume__fill { position: absolute; left: 0; top: 0; width: 64px; height: 4px; border-radius: 2px; background: var(--accent); }
  .volume__knob { position: absolute; left: 59px; top: -4px; width: 11px; height: 11px; border-radius: 50%; background: var(--text); }
</style>
</head>
<body>

<div class="cover-art art-fill" role="img" aria-label="Podcast cover: glitched red and black photograph of two rats">
  <span class="cover-art__title">Silent<br>Moths</span>
</div>

<section class="player">
  <div class="status-bar abs">
    <div class="status-bar__carrier abs">
      <svg width="36" height="8" viewBox="0 0 36 8"><g fill="#fff"><circle cx="4" cy="4" r="3.3"/><circle cx="11" cy="4" r="3.3"/><circle cx="18" cy="4" r="3.3"/><circle cx="25" cy="4" r="3.3"/></g><circle cx="32" cy="4" r="2.8" fill="none" stroke="#fff"/></svg>
      <span>NORTHTEL</span>
      <svg width="13" height="10" viewBox="0 0 13 10" fill="none" stroke="#fff" stroke-width="1.4"><path d="M1 3.5a8 8 0 0 1 11 0M3 5.8a5 5 0 0 1 7 0"/><circle cx="6.5" cy="8.3" r="1" fill="#fff" stroke="none"/></svg>
    </div>
    <div class="status-bar__time abs">4:21 PM</div>
    <div class="status-bar__battery abs">
      <svg width="7" height="12" viewBox="0 0 7 12" fill="none" stroke="#aab3ba" stroke-width="1"><path d="M1 3.5l5 5-2.5 2.5V1L6 3.5l-5 5"/></svg>
      <span>22%</span>
      <svg width="26" height="11" viewBox="0 0 26 11"><rect x=".5" y=".5" width="22" height="10" rx="2" fill="none" stroke="#fff"/><rect x="2" y="2" width="4.5" height="7" fill="#fff"/><rect x="23.5" y="3.5" width="1.5" height="4" fill="#fff"/></svg>
    </div>
  </div>

  <svg class="header__back abs" width="10" height="16" viewBox="0 0 10 16" fill="none" stroke="#fff" stroke-width="1.5"><path d="M8 1L1.5 8 8 15"/></svg>
  <div class="header__title abs">Now Playing</div>
  <svg class="header__search abs" width="16" height="16" viewBox="0 0 16 16" fill="none" stroke="#fff" stroke-width="1.5"><circle cx="6.8" cy="6.8" r="5.6"/><path d="M11 11l4 4"/></svg>

  <div class="episode-art abs art-fill" role="img" aria-label="Episode artwork: glitched red and black photograph of two rats">
    <span class="episode-art__title">Silent<br>Moths</span>
  </div>

  <p class="episode-meta episode-meta--tag abs">Gritty, Modern True Crime Podcast</p>
  <h1 class="episode-meta episode-meta--title abs">Silent Moths - True Crime Podcast</h1>
  <p class="episode-meta episode-meta--info abs">Some Information Here</p>

  <div class="divider abs" style="top:402px"></div>

  <svg class="transport abs" width="347" height="60" viewBox="0 0 347 60">
    <g fill="#fff">
      <path d="M113 20v18l-10-9zM123 20v18l-10-9z"/>
      <path d="M224 20v18l10-9zM234 20v18l10-9z"/>
      <path d="M166 18v22l17-11z"/>
    </g>
    <circle cx="173" cy="29" r="28.5" fill="none" stroke="#fff" stroke-width="1.3"/>
  </svg>

  <div class="progress abs"><div class="progress__fill"></div><div class="progress__handle"></div></div>
  <div class="time time--elapsed abs">31:14</div>
  <div class="time time--total abs">45:00</div>

  <div class="divider abs" style="top:561px"></div>

  <svg class="abs" style="left:21px;top:583px" width="18" height="12" viewBox="0 0 18 12" fill="none" stroke="#1a93e0" stroke-width="1.6"><path d="M0 2h4l8 8h5M0 10h4l8-8h5M14 0l3 2-3 2M14 8l3 2-3 2"/></svg>
  <svg class="abs" style="left:77px;top:583px" width="15" height="12" viewBox="0 0 15 12"><path d="M0 4h3l4-3.5v11L3 8H0z" fill="#fff"/><path d="M9.5 3.5a3.5 3.5 0 0 1 0 5M11.5 1.5a6.5 6.5 0 0 1 0 9" fill="none" stroke="#fff" stroke-width="1.2"/></svg>
  <div class="volume abs"><div class="volume__fill"></div><div class="volume__knob"></div></div>
  <svg class="abs" style="left:311px;top:582px" width="14" height="14" viewBox="0 0 14 14" fill="none" stroke="#fff" stroke-width="1.6"><path d="M11.5 5A5 5 0 1 0 12 8"/><path d="M12 1.5V5H8.5" stroke-width="1.4"/></svg>
</section>

</body>
</html>
```